Talwick Orsine Beauty brand redesign of product labels

national rebrand of skincare product labels - same design but 6 sizes. Will be used for facial serums, body oils, bath salts, room sprays, etc. All labels to be same design - just adjusted for the different sizes. See brand document and sample label.

Bottle Specifications are located in the branding file.
Fonts included in product branding document.
Colours included in branding document.

Featuring company name and logo, product name, product feature, ingredients, size, directions, tag line. See attached sample label as example for design.

Black label base - matt.

Target Market(s)

Natural beauty, 20-60

Industry/Entity Type

farming, natural beauty

Font styles to use
Sans Serif

Requirements
Must have
• Modern, clean, homey
Nice to have
• modern clean design - using the branding colours provided
Should not have
• busy, crowded,

```html
<!DOCTYPE html>
<html lang="en">
<head>
<meta charset="utf-8">
<title>Talwick Orsine Beauty – Vitamin C Green Tea Extract Label</title>
<link rel="stylesheet" href="https://fonts.googleapis.com/css2?family=Montserrat:wght@300;400;600&family=Raleway:wght@300&display=swap">
<style>
  :root {
    --page: #ffffff;
    --label-black: #000000;
    --sage: #d6e7ab;
    --leaf-light: #c9dfa3;
    --leaf-teal: #7fb0a3;
    --ring-teal: #5f9c95;
    --text-white: #f2f2f2;
  }
  html, body {
    margin: 0;
    padding: 0;
    width: 960px;
    height: 1200px;
    overflow: hidden;
    background: var(--page);
  }
  .canvas {
    position: relative;
    width: 960px;
    height: 1200px;
  }
  .label {
    position: absolute;
    left: 30px;
    top: 407px;
    width: 900px;
    height: 386px;
    background: var(--label-black);
    color: var(--text-white);
    font-family: "Montserrat", sans-serif;
    overflow: hidden;
  }
  .copy-block {
    position: absolute;
    margin: 0;
    font-size: 13px;
    line-height: 17px;
    font-weight: 300;
    letter-spacing: 0.2px;
    white-space: nowrap;
  }
  .copy-block--vitamin { left: 51px; top: 36px; }
  .copy-block--greentea { left: 51px; top: 225px; }
  .copy-block--prep { left: 685px; top: 51px; }
  .copy-block--apply { left: 685px; top: 169px; }
  .term { font-weight: 600; }
  .leaf-area {
    position: absolute;
    background: linear-gradient(135deg, var(--leaf-light), var(--leaf-teal));
    opacity: 0.55;
  }
  .leaf-area--top { left: 246px; top: 0; width: 126px; height: 116px; }
  .leaf-area--bottom { left: 548px; top: 288px; width: 128px; height: 98px; }
  .brand-mark {
    position: absolute;
    left: 378px;
    top: 38px;
    width: 172px;
    height: 172px;
  }
  .brand-ring {
    position: absolute;
    inset: 0;
    border: 2px solid var(--ring-teal);
    border-radius: 50%;
  }
  .brand-name {
    position: absolute;
    inset: 0;
    display: flex;
    flex-direction: column;
    align-items: center;
    justify-content: center;
    font-family: "Raleway", sans-serif;
    font-weight: 300;
    font-size: 17px;
    line-height: 23px;
    letter-spacing: 2.5px;
    color: var(--sage);
    text-align: center;
  }
  .product {
    position: absolute;
    left: 0;
    right: 0;
    top: 229px;
    text-align: center;
  }
  .product-name {
    margin: 0;
    font-weight: 300;
    font-size: 24px;
    line-height: 28px;
    letter-spacing: 0.8px;
    color: var(--sage);
  }
  .product-feature {
    margin: 7px 0 0;
    font-weight: 300;
    font-size: 17px;
    line-height: 23px;
    letter-spacing: 0.6px;
  }
  .product-size {
    margin: 8px 0 0;
    font-weight: 300;
    font-size: 17px;
    line-height: 22px;
  }
</style>
</head>
<body>
<main class="canvas">
  <section class="label">
    <p class="copy-block copy-block--vitamin"><span class="term">Vitamin C (Sodium<br>Ascorbyl<br>Phosphate):</span> A stable<br>form of Vitamin C<br>that brightens the<br>skin and boosts<br>collagen production,<br>making skin look<br>vibrant and youthful.</p>
    <p class="copy-block copy-block--greentea"><span class="term">Green Tea Extract:</span><br>Rich in antioxidants,<br>it helps protect the<br>skin from<br>environmental<br>damage and soothes<br>inflammation.</p>

    <div class="leaf-area leaf-area--top" role="img" aria-label="Illustrated green tea leaf sprig"></div>

    <div class="brand-mark">
      <div class="brand-ring"></div>
      <div class="brand-name"><span>TALWICK</span><span>ORSINE</span><span>BEAUTY</span></div>
    </div>

    <div class="product">
      <h1 class="product-name">VITAMIN C<br>GREEN TEA EXTRACT</h1>
      <p class="product-feature">BRIGHTENING<br>FACIAL COMPLEX</p>
      <p class="product-size">15 ml</p>
    </div>

    <div class="leaf-area leaf-area--bottom" role="img" aria-label="Illustrated green tea leaf sprig"></div>

    <p class="copy-block copy-block--prep"><span class="term">Preparation:</span> Start with a<br>clean, dry face. Cleanse to<br>remove any dirt or oil<br>buildup.</p>
    <p class="copy-block copy-block--apply"><span class="term">Application:</span> Apply 2-3<br>drops of the serum onto<br>your fingertips.<br>Gently pat or massage the<br>serum into your face,<br>focusing on areas with<br>uneven skin tone, dark<br>spots, or dullness.</p>
  </section>
</main>
</body>
</html>
```